Health care center needs brochure design

We need a set of brochure designs for the 4 sections of our clinic, color coded based on the brand guidelines and with introduced icons to every section. The three sections include Biological Medicine (main medication tool is the IV tool), The golden tide program (main medication tool are the detox tools) , the Aesthetics section ( main medication tool is the syringe) and the lab (main tool is the microscope). You can find out more about our sections in the website www.drvelnor.com. The use of elements of the brand itself such as the lotus is also applicable.

Industry/Entity Type

Health Care

Requirements
Must have
• use of brand identity colors and features
• reflective medical icons
• color coding for each of the 4 sections based on the brand colors
Should not have
• pictures overused by other health care providers

```html
<!DOCTYPE html>
<html lang="en">
<head>
<meta charset="utf-8">
<title>Integrated Care Center – Brochure Outside</title>
<link href="https://fonts.googleapis.com/css2?family=Montserrat:wght@400;500;600;700&display=swap" rel="stylesheet">
<style>
  :root {
    --peach: #f0a27c;
    --peach-soft: #f6cdb6;
    --peach-pale: #fbe6da;
    --terracotta: #c8704f;
    --clay-light: #d98b68;
    --mint: #6cc9a0;
    --mint-light: #8fd8b7;
    --mint-pale: #b6e8d2;
    --ink: #1f1f1f;
    --paper: #f4f4f3;
    --stage: #e6e6e6;
    --white: #ffffff;
  }
  * { box-sizing: border-box; margin: 0; padding: 0; }
  html, body { width: 1200px; height: 935px; overflow: hidden; background: var(--stage); }
  body { font-family: "Montserrat", Arial, sans-serif; color: var(--ink); }

  .spread { position: absolute; left: 0; top: 43px; width: 1200px; height: 848px; display: flex; }
  .page { position: relative; width: 600px; height: 848px; background: var(--paper); overflow: hidden; }
  .page svg.page-art { position: absolute; inset: 0; }

  /* Back page */
  .about { position: absolute; left: 32px; top: 327px; width: 536px; }
  .section-title { font-size: 25px; font-weight: 400; letter-spacing: 0.5px; color: var(--peach); }
  .section-title strong { font-weight: 600; }
  .section-title::after { content: ""; display: block; width: 95px; height: 1px; background: var(--peach); margin-top: 3px; }
  .about p { font-size: 12.6px; line-height: 15.7px; text-align: justify; margin-top: 14px; }
  .about p + p { margin-top: 15px; }

  .contact { position: absolute; left: 323px; top: 625px; width: 260px; }
  .contact-title { font-size: 23px; font-weight: 400; color: var(--peach); }
  .contact-title strong { color: var(--mint); font-weight: 600; }
  .contact-title::after { content: ""; display: block; width: 36px; height: 1px; background: var(--peach); margin-top: 2px; }
  .contact ul { list-style: none; margin-top: 8px; font-size: 12.8px; line-height: 15.6px; }
  .contact li { position: relative; padding-left: 22px; margin-bottom: 4px; }
  .contact li svg { position: absolute; left: 0; top: 2px; width: 12px; height: 12px; }

  .brand { position: absolute; display: flex; align-items: center; }
  .brand-dot { border-radius: 50%; background: var(--peach); flex: none; }
  .brand-name { font-weight: 500; color: var(--mint); text-transform: uppercase; }
  .brand--small { left: 32px; top: 692px; gap: 12px; }
  .brand--small .brand-dot { width: 96px; height: 96px; }
  .brand--small .brand-name { font-size: 15px; line-height: 17px; }
  .brand--large { left: 155px; top: 627px; gap: 16px; }
  .brand--large .brand-dot { width: 150px; height: 150px; }
  .brand--large .brand-name { font-size: 22px; line-height: 25px; }

  /* Front page */
  .welcome { position: absolute; right: 35px; top: 322px; text-align: right; color: var(--white); }
  .welcome span { display: block; font-size: 28px; font-weight: 400; }
  .welcome h1 { font-size: 33px; line-height: 39px; font-weight: 700; }
  .site-url { position: absolute; left: 0; right: 0; bottom: 14px; text-align: center; color: var(--white); font-size: 17px; letter-spacing: 4px; }
</style>
</head>
<body>
<main class="spread">

  <section class="page page--back">
    <svg class="page-art" width="600" height="848" viewBox="0 0 600 848">
      <defs>
        <linearGradient id="portraitTone" x1="0" y1="0" x2="0" y2="1">
          <stop offset="0" stop-color="#dcd9d5"/>
          <stop offset="1" stop-color="#ecebe9"/>
        </linearGradient>
      </defs>
      <g fill="var(--peach)" opacity="0.18">
        <circle cx="45" cy="134" r="35"/>
        <circle cx="79" cy="175" r="20"/>
        <circle cx="136" cy="152" r="44"/>
        <circle cx="468" cy="310" r="44"/>
        <circle cx="520" cy="330" r="30"/>
      </g>
      <circle cx="309" cy="155" r="184" fill="none" stroke="var(--peach-pale)" stroke-width="10"/>
      <circle cx="309" cy="155" r="173" fill="none" stroke="var(--mint)" stroke-width="6"/>
      <circle cx="309" cy="155" r="168" fill="url(#portraitTone)" role="img" aria-label="Portrait of the center's founding doctor in a white coat"/>
      <rect width="600" height="13" fill="var(--peach-soft)"/>
      <path d="M0 660 Q250 560 560 610" fill="none" stroke="var(--peach-pale)" stroke-width="18" opacity="0.8"/>
      <g class="section-bands">
        <path d="M0 800 H160 L148 848 H0 Z" fill="var(--mint)"/>
        <path d="M160 800 H240 L228 848 H148 Z" fill="var(--mint-light)"/>
        <path d="M240 800 H320 L308 848 H228 Z" fill="var(--mint-pale)"/>
        <path d="M320 800 H385 L370 848 H308 Z" fill="var(--mint-light)"/>
        <path d="M398 800 H470 L458 848 H383 Z" fill="var(--clay-light)"/>
        <path d="M470 800 H540 L528 848 H458 Z" fill="#d07c5a"/>
        <path d="M540 800 H600 V848 H528 Z" fill="var(--terracotta)"/>
      </g>
    </svg>

    <article class="about">
      <h2 class="section-title">ABOUT <strong>THE CENTER</strong></h2>
      <p>We are proud to be the first to provide alternative biologocal medicine in the region integrated with programs that envelope the healing process in a complete cycle touching The Body, The Mind and The Soul. The Center provides access to new ways of healing via Ayurverdic medicine and Aesthetic procedures. It also provides new diagnostics and regime treatments to encompass the needs of your body taking it towards its natural healthy state in a happy purified mind and soul.</p>
      <p>Created to be your healing getaway, the center is set to make you feel welcome and at ease from the moment you step in. We wish to ensure your steps towards a better tranformed you starts with a smile. We aim to see you glowing with the beautiful life within you and to guide you bring out the best in your natural self.</p>
    </article>

    <aside class="contact">
      <h3 class="contact-title">Get in <strong>Touch</strong></h3>
      <ul>
        <li>Dr Sara Velnor Integrated Care Center POBox 40321</li>
        <li><svg viewBox="0 0 12 12"><path d="M6 0.5a4 4 0 0 0-4 4c0 3 4 7 4 7s4-4 4-7a4 4 0 0 0-4-4z" fill="var(--peach)"/><circle cx="6" cy="4.5" r="1.4" fill="#fff"/></svg>Coral District, Harbor Road, Marina South, Seaview Bay</li>
        <li><svg viewBox="0 0 12 12"><circle cx="6" cy="6" r="6" fill="var(--peach)"/><path d="M4 3.2l1.1 1.3-.6.8c.4.9 1.1 1.6 2 2l.8-.6 1.3 1.1-.6 1c-2.3-.3-4.2-2.2-4.5-4.5z" fill="#fff"/></svg>02-555 0147</li>
        <li><svg viewBox="0 0 12 12"><circle cx="6" cy="6" r="6" fill="var(--peach)"/><rect x="3" y="4" width="6" height="4.2" fill="#fff"/><path d="M3 4l3 2.3L9 4" fill="none" stroke="var(--peach)" stroke-width=".7"/></svg>info@drvelnor.com</li>
        <li><svg viewBox="0 0 12 12"><circle cx="6" cy="6" r="6" fill="var(--peach)"/><rect x="3" y="3.6" width="6" height="4.6" rx=".6" fill="#fff"/></svg>www.drvelnor.com</li>
      </ul>
    </aside>

    <div class="brand brand--small">
      <span class="brand-dot"></span>
      <span class="brand-name">Dr. Sara Velnor<br>Integrated<br>Care Center</span>
    </div>
  </section>

  <section class="page page--front">
    <svg class="page-art" width="600" height="848" viewBox="0 0 600 848">
      <defs>
        <radialGradient id="landscapeTone" cx="0.5" cy="0.55" r="0.6">
          <stop offset="0" stop-color="#5e8a3a"/>
          <stop offset="1" stop-color="#3f5a26"/>
        </radialGradient>
        <linearGradient id="peachWash" x1="0" y1="0" x2="1" y2="1">
          <stop offset="0" stop-color="#f2b192"/>
          <stop offset="1" stop-color="#f7d3c0"/>
        </linearGradient>
      </defs>
      <path d="M0 0 H230 L170 170 L0 500 Z" fill="url(#peachWash)"/>
      <path d="M0 0 H130 L0 270 Z" fill="#eea07c" opacity="0.6"/>
      <path d="M0 640 Q300 730 600 590" fill="none" stroke="var(--peach-pale)" stroke-width="36" opacity="0.6"/>
      <circle cx="435" cy="229" r="370" fill="none" stroke="var(--mint)" stroke-width="9"/>
      <circle cx="435" cy="229" r="354" fill="none" stroke="var(--peach-pale)" stroke-width="14"/>
      <circle cx="435" cy="229" r="338" fill="none" stroke="var(--peach-soft)" stroke-width="6" stroke-dasharray="220 60"/>
      <circle cx="435" cy="229" r="325" fill="url(#landscapeTone)" role="img" aria-label="Green valley with a village and wooded mountain under an overcast sky"/>
      <g class="section-bands">
        <rect y="800" width="90" height="48" fill="var(--terracotta)"/>
        <path d="M90 800 H300 L288 848 H90 Z" fill="var(--clay-light)"/>
        <path d="M300 800 H600 V848 H288 Z" fill="var(--terracotta)"/>
      </g>
    </svg>

    <div class="welcome">
      <span>Welcome to</span>
      <h1>The First and<br>Only Integrative<br>Center of its kind<br>in the Region</h1>
    </div>

    <div class="brand brand--large">
      <span class="brand-dot"></span>
      <span class="brand-name">Dr. Sara Velnor<br>Integrated<br>Care Center</span>
    </div>

    <p class="site-url">www.drvelnor.com</p>
  </section>

</main>
</body>
</html>
```